International Flower distributer needs a landing page

We are looking to have a landing page made that will be easy to maintain and upload more content as our business grows.

We like the template designs and ease of use of Pagewright. We'd explore other host sites.

Hello,

To start we would like something that can be managed and updated on a platform like pagewright. We like page wright because of the premade designs and flexibility.

Website requirements:

- About us:

- Marlowe Vantage Corp - Established 1999

- Verna Holt - Founder

- Danielle Holt - Account Executive

- Gregory Holt - Director of Operations

- Pilar Wendham - (Jo's Job Description?)

- Renata Valcourt (Make us look like a bigger company with more staff)

What we do:

- Personalized Customer service

- Exclusively Mass market experience to meet high demands

- Dedicated team assigned to your account

How we do it:

- Partnerships with farms in COlombia, ecuador and costa rica

- Farm fresh delivered directly from cargo planes to state of the art cooler facility at Delmont Airport

- Verity Trust?

Products we Sell:

- Farm made bouquets

- Consumer Bunches

- Programs Tailored to fit customer's retail program

For more Information:

- Gregory and Danielle phone and email

- Submit email inquiry

Gathering more feedback

Corporate buyers that want to verify who we are and get our contact information

Floral, but not a flower shop. We import farm fresh cut flowers from south america and send them directly to supermarkets around the country.

• We are not selling anything on the website. We sell business to business.

```html
<!DOCTYPE html>
<html lang="en">
<head>
<meta charset="utf-8">
<title>Marlowe Vantage — Farm Fresh Cut Flowers from South America</title>
<link href="https://fonts.googleapis.com/css2?family=Poppins:ital,wght@0,300;0,400;0,500;0,600;0,700;0,800;1,400&family=Dancing+Script:wght@600&display=swap" rel="stylesheet">
<style>
:root{
  --indigo:#3a2fb6;
  --indigo-deep:#2b2399;
  --navy:#23207a;
  --green:#7cc243;
  --green-dark:#5fa52a;
  --ink:#2b2b3a;
  --muted:#6f6f80;
  --line:#e4e4ee;
  --white:#ffffff;
}
*{box-sizing:border-box;margin:0;padding:0}
html,body{width:1200px;height:4316px;overflow:hidden}
body{font-family:"Poppins",sans-serif;color:var(--ink);background:var(--white);position:relative}
.abs{position:absolute}
.btn{display:inline-flex;align-items:center;justify-content:center;gap:8px;border-radius:30px;font-size:11px;font-weight:600;letter-spacing:.8px;text-transform:uppercase}
.btn-green{background:var(--green);color:#fff;height:34px;padding:0 26px}
.btn-outline{border:1.5px solid var(--green);color:var(--green);height:30px;padding:0 22px;background:#fff}

/* header */
.site-header{top:0;left:0;width:1200px;height:60px;background:#fff;display:flex;align-items:center;padding:0 160px;z-index:3}
.brand{display:flex;align-items:center;gap:8px;font-weight:700;font-size:15px;line-height:1.05;color:var(--indigo);text-transform:uppercase}
.brand-dot{width:26px;height:26px;border-radius:50%;background:var(--indigo)}
.main-nav{display:flex;gap:26px;margin-left:auto;align-items:center;font-size:10.5px;font-weight:600;color:var(--navy);text-transform:uppercase}
.main-nav .active{border-bottom:2px solid var(--green);padding-bottom:3px}
.nav-cta{border:1.5px solid var(--indigo);color:var(--indigo);border-radius:20px;padding:6px 14px;display:flex;align-items:center;gap:6px}

/* hero */
.hero{top:60px;left:0;width:1200px;height:440px;overflow:hidden}
.hero-photo{position:absolute;inset:0;background:radial-gradient(circle at 10% 20%,#f6f8fb 0 90px,transparent 160px),radial-gradient(circle at 90% 30%,#f4f6f9 0 100px,transparent 170px),radial-gradient(circle at 85% 85%,#eef2f6 0 80px,transparent 150px),linear-gradient(180deg,#bcd3e6 0%,#cfdeec 60%,#dfe8f1 100%)}
.hero-copy{position:absolute;top:105px;left:0;width:1200px;text-align:center}
.hero-kicker{font-size:25px;font-weight:600;color:var(--green-dark);text-transform:uppercase;letter-spacing:.5px}
.hero-title{font-size:54px;font-weight:800;color:var(--navy);text-transform:uppercase;line-height:1.1;margin-top:2px}
.hero-sub{font-size:16px;color:var(--navy);margin-top:10px}
.hero .btn{margin-top:22px}
.hero-wave{position:absolute;left:0;bottom:0}

/* about */
.about-ring{left:150px;top:600px;width:360px;height:360px;border-radius:50%;background:radial-gradient(circle,#fff 0 110px,#ece9f7 111px 118px,#5c4aa8 119px,#3d2f86 70%,#6f5cb8 100%);box-shadow:0 0 0 6px #fff,0 0 0 7px #dedbea}
.about-text{left:590px;top:612px;width:480px}
.est{font-family:"Dancing Script",cursive;font-size:20px;color:var(--green-dark)}
.section-title{font-size:40px;font-weight:400;color:var(--navy);text-transform:uppercase;line-height:1.1}
.section-title b{font-weight:800}
.about-text p{font-size:11.5px;line-height:1.75;color:var(--muted);margin-top:12px}
.about-text .btn{margin-top:22px}

/* team */
.team-card{top:1060px;width:208px;height:262px;border-radius:10px;overflow:hidden}
.team-photo{width:100%;height:100%}
.team-overlay{position:absolute;inset:0;background:rgba(58,47,182,.88);color:#fff;display:flex;flex-direction:column;align-items:center;justify-content:center;padding:24px;text-align:center;font-size:11px;line-height:1.6}
.socials{display:flex;gap:10px;margin-top:14px}
.socials span{width:12px;height:12px;border-radius:50%;background:#fff}
.team-name{top:1338px;width:208px;text-align:center}
.team-name h4{font-size:14px;font-weight:700;color:var(--navy);text-transform:uppercase}
.team-name p{font-size:11px;color:var(--muted);margin-top:2px}
.slider-arrow{top:1175px;width:30px;height:30px;border-radius:50%;border:1px solid #c9c9d6;display:flex;align-items:center;justify-content:center;background:#fff}
.view-staff{top:1412px;left:0;width:1200px;text-align:center}

/* what we do */
.what-we-do{top:1528px;left:0;width:1200px;height:1272px;background:linear-gradient(180deg,#3a30b8 0%,#3228aa 50%,#2c2396 100%)}
.wwd-title{top:1590px;left:0;width:1200px;text-align:center;color:#fff}
.wwd-title .section-title{color:#fff}
.wwd-photo{border-radius:50%;box-shadow:0 0 0 8px rgba(255,255,255,.12)}
.wwd-arc{overflow:visible}
.wwd-item{width:440px;color:#fff}
.wwd-item h3{font-size:15px;font-weight:700;text-transform:uppercase;line-height:1.35;margin-top:14px}
.wwd-item p{font-size:11px;line-height:1.8;color:#d9d6f4;margin-top:10px}
.wwd-icon{width:42px;height:42px}

/* how we do it */
.hwdi-title{top:2880px;left:0;width:1200px;text-align:center}
.step{top:2960px;width:260px;text-align:center}
.step-badge{width:96px;height:96px;margin:0 auto}
.step p{font-size:11.5px;line-height:1.6;color:var(--ink);margin-top:16px}

/* products */
.products{top:3200px;left:0;width:1200px;height:790px;background:radial-gradient(ellipse at 20% 90%,#6a6d1c 0,transparent 300px),radial-gradient(ellipse at 85% 80%,#7a6a14 0,transparent 320px),linear-gradient(180deg,#141514 0%,#1e2116 45%,#37401c 100%)}
.products-title{top:3270px;left:0;width:1200px;text-align:center}
.products-title .section-title{color:#fff}
.product-card{top:3340px;width:280px;height:480px;background:#fff;border-radius:10px;overflow:hidden;text-align:center}
.product-photo{height:200px;margin:12px 12px 0;border-radius:8px}
.product-card h3{font-size:14px;font-weight:700;color:var(--navy);text-transform:uppercase;margin-top:26px}
.product-card p{font-size:11px;line-height:1.75;color:var(--muted);margin:12px 28px 0}
.view-more{display:inline-flex;align-items:center;gap:6px;font-size:11px;font-weight:700;color:var(--navy);text-transform:uppercase;margin-top:26px}
.products-cta{top:3890px;left:0;width:1200px;text-align:center}

/* enquiry */
.enquiry{top:4010px;left:0;width:1200px;text-align:center}
.enquiry h2{font-size:17px;font-weight:700;color:var(--navy);text-transform:uppercase}
.enquiry-form{display:flex;justify-content:center;gap:10px;margin-top:18px}
.enquiry-input{width:330px;height:36px;border:1px solid var(--line);border-radius:20px;font-size:11px;color:#9a9aab;text-align:left;padding:0 18px;display:flex;align-items:center}
.contacts{top:4150px;left:160px;width:880px;display:flex;justify-content:space-between;border-top:1px solid var(--line);padding-top:24px}
.contact{display:flex;align-items:center;gap:10px}
.contact-icon{width:34px;height:34px;border-radius:50%;background:var(--indigo);display:flex;align-items:center;justify-content:center}
.contact small{display:block;font-size:10px;color:var(--muted)}
.contact strong{display:block;font-size:11.5px;font-weight:600;color:var(--navy)}
.copyright{top:4270px;left:0;width:1200px;text-align:center;font-size:10.5px;color:var(--muted)}
</style>
</head>
<body>

<header class="site-header abs">
  <div class="brand"><span class="brand-dot"></span><span>Marlowe<br>Vantage</span></div>
  <nav class="main-nav">
    <span class="active">Home</span><span>About Us</span><span>What We Do</span><span>How We Do It</span><span>Product We Sell</span>
    <span class="nav-cta"><svg width="11" height="11" viewBox="0 0 24 24"><path d="M6.6 10.8a15 15 0 0 0 6.6 6.6l2.2-2.2a1 1 0 0 1 1-.25 11.4 11.4 0 0 0 3.6.57 1 1 0 0 1 1 1V20a1 1 0 0 1-1 1A17 17 0 0 1 3 4a1 1 0 0 1 1-1h3.5a1 1 0 0 1 1 1c0 1.25.2 2.45.57 3.57a1 1 0 0 1-.25 1z" fill="#3a2fb6"/></svg>Let's Talk</span>
  </nav>
</header>

<section class="hero abs">
  <div class="hero-photo" role="img" aria-label="White blossom branches over a pale blue wooden surface"></div>
  <div class="hero-copy">
    <div class="hero-kicker">We import farm fresh cut flowers</div>
    <h1 class="hero-title">From South America</h1>
    <p class="hero-sub">send them directly to supermarkets around the country.</p>
    <span class="btn btn-green">Learn More <svg width="10" height="10" viewBox="0 0 10 10"><path d="M1 5h7M5 2l3 3-3 3" stroke="#fff" stroke-width="1.6" fill="none"/></svg></span>
  </div>
  <svg class="hero-wave" width="1200" height="70" viewBox="0 0 1200 70"><path d="M0 40 C200 0 350 70 600 40 S1000 10 1200 45 V70 H0Z" fill="#fff"/></svg>
</section>

<section class="about">
  <div class="about-ring abs" role="img" aria-label="Circular frame of purple flowers around the company emblem"></div>
  <div class="about-text abs">
    <div class="est">Established in 1999</div>
    <h2 class="section-title">About <b>Us</b></h2>
    <p>Marlowe Vantage Corp has brought fresh cut flowers from trusted growers to retail shelves for more than two decades. We work closely with every partner farm, follow each shipment from harvest to store and keep quality high so buyers can rely on steady supply all year.</p>
    <p>Our team pairs deep market knowledge with careful handling, giving supermarkets across the country fresh stems, fair pricing and service they can count on.</p>
    <span class="btn btn-green">Learn More <svg width="10" height="10" viewBox="0 0 10 10"><path d="M1 5h7M5 2l3 3-3 3" stroke="#fff" stroke-width="1.6" fill="none"/></svg></span>
  </div>

  <div class="slider-arrow abs" style="left:115px"><svg width="10" height="10" viewBox="0 0 10 10"><path d="M6.5 1.5 3 5l3.5 3.5" stroke="#6f6f80" stroke-width="1.4" fill="none"/></svg></div>
  <div class="slider-arrow abs" style="left:1055px"><svg width="10" height="10" viewBox="0 0 10 10"><path d="M3.5 1.5 7 5 3.5 8.5" stroke="#6f6f80" stroke-width="1.4" fill="none"/></svg></div>

  <div class="team-card abs" style="left:160px"><div class="team-photo" role="img" aria-label="Portrait of Verna Holt" style="background:linear-gradient(160deg,#8a8f96,#4a4d55)"></div></div>
  <div class="team-card abs" style="left:388px"><div class="team-photo" role="img" aria-label="Portrait of Danielle Holt" style="background:linear-gradient(160deg,#a79a8c,#5e544b)"></div>
    <div class="team-overlay">Keeps every account running smoothly and on time.<div class="socials"><span></span><span></span><span></span></div></div></div>
  <div class="team-card abs" style="left:616px"><div class="team-photo" role="img" aria-label="Portrait of Gregory Holt" style="background:linear-gradient(160deg,#8fae86,#4f6a4a)"></div></div>
  <div class="team-card abs" style="left:840px"><div class="team-photo" role="img" aria-label="Portrait of Pilar Wendham" style="background:linear-gradient(160deg,#7e6a5e,#3e3532)"></div></div>

  <div class="team-name abs" style="left:160px"><h4>Verna Holt</h4><p>Founder</p></div>
  <div class="team-name abs" style="left:388px"><h4>Danielle Holt</h4><p>Account Executive</p></div>
  <div class="team-name abs" style="left:616px"><h4>Gregory Holt</h4><p>Director of Operations</p></div>
  <div class="team-name abs" style="left:840px"><h4>Pilar Wendham</h4><p>Jo's Job Description</p></div>

  <div class="view-staff abs"><span class="btn btn-outline">View All Staff <svg width="10" height="10" viewBox="0 0 10 10"><path d="M1 5h7M5 2l3 3-3 3" stroke="#7cc243" stroke-width="1.6" fill="none"/></svg></span></div>
</section>

<section class="what-we-do abs"></section>
<div class="wwd-title abs"><h2 class="section-title">What <b>We Do</b></h2></div>

<svg class="wwd-arc abs" style="left:140px;top:1680px" width="400" height="420" viewBox="0 0 400 420"><path d="M40 80 A190 190 0 0 1 330 60" stroke="#fff" stroke-width="1.5" stroke-dasharray="5 5" fill="none"/><path d="M322 52l10 8-12 4" stroke="#fff" stroke-width="1.5" fill="none"/></svg>
<div class="wwd-photo abs" style="left:160px;top:1710px;width:360px;height:360px;background:linear-gradient(150deg,#c9a07c,#7a5a44)" role="img" aria-label="Advisor meeting with a couple at a desk"></div>
<div class="wwd-item abs" style="left:590px;top:1750px">
  <svg class="wwd-icon" viewBox="0 0 42 42"><rect x="6" y="8" width="30" height="22" rx="2" stroke="#fff" stroke-width="2" fill="none"/><path d="M14 36h14M21 30v6" stroke="#fff" stroke-width="2"/><circle cx="21" cy="17" r="4" stroke="#fff" stroke-width="2" fill="none"/></svg>
  <h3>Personalized Customer Service</h3>
  <p>Every buyer gets direct contact with people who know their stores, their volumes and their calendar. We answer fast, plan ahead with you and adjust orders as demand shifts through the season.</p>
</div>

<div class="wwd-item abs" style="left:160px;top:2150px">
  <svg class="wwd-icon" viewBox="0 0 42 42"><path d="M6 34h30M10 34V20M18 34V14M26 34V22M34 34V10" stroke="#fff" stroke-width="2"/></svg>
  <h3>Exclusively Mass Market Experience to<br>Meet High Demands</h3>
  <p>We supply large retail chains only, so our sourcing, packing and logistics are built for high volume. Peak holidays and weekly programs run on the same steady process without gaps.</p>
</div>
<svg class="wwd-arc abs" style="left:670px;top:2070px" width="400" height="400" viewBox="0 0 400 400"><path d="M60 40 A190 190 0 0 1 370 150" stroke="#fff" stroke-width="1.5" stroke-dasharray="5 5" fill="none"/><path d="M52 34l12 2-6 10" stroke="#fff" stroke-width="1.5" fill="none"/></svg>
<div class="wwd-photo abs" style="left:690px;top:2090px;width:360px;height:360px;background:linear-gradient(150deg,#e7a4b8,#b84a6a 55%,#6e7b3a)" role="img" aria-label="Buckets of mixed fresh flowers at a market stall"></div>

<svg class="wwd-arc abs" style="left:140px;top:2380px" width="400" height="400" viewBox="0 0 400 400"><path d="M30 140 A190 190 0 0 1 300 30" stroke="#fff" stroke-width="1.5" stroke-dasharray="5 5" fill="none"/><path d="M292 22l12 6-10 8" stroke="#fff" stroke-width="1.5" fill="none"/></svg>
<div class="wwd-photo abs" style="left:160px;top:2400px;width:350px;height:350px;background:linear-gradient(150deg,#d9c3b0,#8c6b57)" role="img" aria-label="Smiling support agent wearing a headset"></div>
<div class="wwd-item abs" style="left:590px;top:2500px">
  <svg class="wwd-icon" viewBox="0 0 42 42"><circle cx="14" cy="14" r="5" stroke="#fff" stroke-width="2" fill="none"/><circle cx="28" cy="14" r="5" stroke="#fff" stroke-width="2" fill="none"/><path d="M4 34c0-6 4-10 10-10s10 4 10 10M18 34c0-6 4-10 10-10s10 4 10 10" stroke="#fff" stroke-width="2" fill="none"/></svg>
  <h3>Dedicated Team Assigned to Your Account</h3>
  <p>A small group of specialists stays with your account from first order onward. They know your programs, track every delivery and keep you informed at each step of the way.</p>
</div>

<section class="how-we-do-it">
  <div class="hwdi-title abs"><h2 class="section-title">How <b>We Do It</b></h2></div>
  <svg class="abs" style="left:390px;top:2985px" width="140" height="40" viewBox="0 0 140 40"><path d="M5 30 Q70 -5 130 25" stroke="#9a9aab" stroke-width="1.4" stroke-dasharray="4 4" fill="none"/><path d="M122 18l9 7-11 3" stroke="#9a9aab" stroke-width="1.4" fill="none"/></svg>
  <svg class="abs" style="left:690px;top:2985px" width="140" height="40" viewBox="0 0 140 40"><path d="M5 30 Q70 -5 130 25" stroke="#9a9aab" stroke-width="1.4" stroke-dasharray="4 4" fill="none"/><path d="M122 18l9 7-11 3" stroke="#9a9aab" stroke-width="1.4" fill="none"/></svg>

  <div class="step abs" style="left:180px">
    <svg class="step-badge" viewBox="0 0 96 96"><path d="M48 4 C72 30 86 46 86 62 A38 38 0 0 1 10 62 C10 46 24 30 48 4Z" fill="#7cc243"/><path d="M30 60l10-8 8 6 8-6 10 8M40 52l8-6 8 6" stroke="#fff" stroke-width="3" fill="none" stroke-linecap="round" stroke-linejoin="round"/></svg>
    <p>Partnerships with farms in Colombia,<br>ecuador and costa rica</p>
  </div>
  <div class="step abs" style="left:470px">
    <svg class="step-badge" viewBox="0 0 96 96"><path d="M48 4 C72 30 86 46 86 62 A38 38 0 0 1 10 62 C10 46 24 30 48 4Z" fill="#7cc243"/><path d="M26 62l44-16-4-4-14 3-12-10h-5l7 13-10 3-5-4h-4l4 8z" fill="#fff"/></svg>
    <p>Farm fresh delivered directly from cargo planes to state of the art cooler facility of Delmont Airport</p>
  </div>
  <div class="step abs" style="left:760px">
    <svg class="step-badge" viewBox="0 0 96 96"><path d="M48 4 C72 30 86 46 86 62 A38 38 0 0 1 10 62 C10 46 24 30 48 4Z" fill="#7cc243"/><path d="M34 60l10 10 20-22" stroke="#fff" stroke-width="4" fill="none" stroke-linecap="round" stroke-linejoin="round"/></svg>
    <p>Verity Trust?</p>
  </div>
</section>

<section class="products abs" role="img" aria-label="Field of yellow and red tulips under a dark sky"></section>
<div class="products-title abs"><h2 class="section-title">Product <b>We Sell</b></h2></div>

<div class="product-card abs" style="left:160px">
  <div class="product-photo" role="img" aria-label="Hands arranging a fresh bouquet" style="background:linear-gradient(150deg,#c98e74,#6e4a3a)"></div>
  <h3>Farm Made Bouquets</h3>
  <p>Hand built at the farm and packed to arrive shelf ready for your floral aisle.</p>
  <span class="view-more">View More <svg width="10" height="10" viewBox="0 0 10 10"><path d="M1 5h7M5 2l3 3-3 3" stroke="#23207a" stroke-width="1.6" fill="none"/></svg></span>
</div>
<div class="product-card abs" style="left:460px">
  <div class="product-photo" role="img" aria-label="Bunches of red and pink roses" style="background:linear-gradient(150deg,#d06a7a,#7a2c3a)"></div>
  <h3>Consumer Bunches</h3>
  <p>Simple single variety bunches sleeved and graded for quick everyday sale.</p>
  <span class="view-more">View More <svg width="10" height="10" viewBox="0 0 10 10"><path d="M1 5h7M5 2l3 3-3 3" stroke="#23207a" stroke-width="1.6" fill="none"/></svg></span>
</div>
<div class="product-card abs" style="left:760px">
  <div class="product-photo" role="img" aria-label="Woman holding a bouquet in a bright store" style="background:linear-gradient(150deg,#cfd8e6,#8a9cb8)"></div>
  <h3>Customer's Retail Program</h3>
  <p>Programs tailored to fit each retailer's stores, volumes and seasonal plans.</p>
  <span class="view-more">View More <svg width="10" height="10" viewBox="0 0 10 10"><path d="M1 5h7M5 2l3 3-3 3" stroke="#23207a" stroke-width="1.6" fill="none"/></svg></span>
</div>
<div class="products-cta abs"><span class="btn btn-green">Learn More <svg width="10" height="10" viewBox="0 0 10 10"><path d="M1 5h7M5 2l3 3-3 3" stroke="#fff" stroke-width="1.6" fill="none"/></svg></span></div>

<section class="enquiry abs">
  <h2>Check Your Valid Enquiry</h2>
  <div class="enquiry-form">
    <div class="enquiry-input">Enter Your email</div>
    <span class="btn btn-green" style="height:36px">Submit Enquiry <svg width="10" height="10" viewBox="0 0 10 10"><path d="M1 5h7M5 2l3 3-3 3" stroke="#fff" stroke-width="1.6" fill="none"/></svg></span>
  </div>
</section>

<div class="contacts abs">
  <div class="contact"><span class="contact-icon"><svg width="14" height="14" viewBox="0 0 24 24"><path d="M6.6 10.8a15 15 0 0 0 6.6 6.6l2.2-2.2a1 1 0 0 1 1-.25 11.4 11.4 0 0 0 3.6.57 1 1 0 0 1 1 1V20a1 1 0 0 1-1 1A17 17 0 0 1 3 4a1 1 0 0 1 1-1h3.5a1 1 0 0 1 1 1c0 1.25.2 2.45.57 3.57a1 1 0 0 1-.25 1z" fill="#fff"/></svg></span><div><small>Call Gregory Holt</small><strong>(555) 014-2290</strong></div></div>
  <div class="contact"><span class="contact-icon"><svg width="14" height="14" viewBox="0 0 24 24"><path d="M6.6 10.8a15 15 0 0 0 6.6 6.6l2.2-2.2a1 1 0 0 1 1-.25 11.4 11.4 0 0 0 3.6.57 1 1 0 0 1 1 1V20a1 1 0 0 1-1 1A17 17 0 0 1 3 4a1 1 0 0 1 1-1h3.5a1 1 0 0 1 1 1c0 1.25.2 2.45.57 3.57a1 1 0 0 1-.25 1z" fill="#fff"/></svg></span><div><small>Call Danielle Holt</small><strong>(555) 014-2290</strong></div></div>
  <div class="contact"><span class="contact-icon"><svg width="14" height="14" viewBox="0 0 24 24"><rect x="3" y="5" width="18" height="14" rx="2" fill="none" stroke="#fff" stroke-width="2"/><path d="M3 7l9 6 9-6" fill="none" stroke="#fff" stroke-width="2"/></svg></span><div><small>Email Gregory Holt</small><strong>info@marlowevantage.com</strong></div></div>
  <div class="contact"><span class="contact-icon"><svg width="14" height="14" viewBox="0 0 24 24"><rect x="3" y="5" width="18" height="14" rx="2" fill="none" stroke="#fff" stroke-width="2"/><path d="M3 7l9 6 9-6" fill="none" stroke="#fff" stroke-width="2"/></svg></span><div><small>Email Danielle Holt</small><strong>info@marlowevantage.com</strong></div></div>
</div>

<footer class="copyright abs">Copyright © 2022 Marlowe Vantage. All rights reserved.</footer>

</body>
</html>
```